fizzy drinks label design

I want to design fizzy drink label for 3 flavors : black grapes, red apple and mojito, band name kestrola, product name KOLTA , product will be in plastic bottle, label size 198 mm X 66mm

```html
<!DOCTYPE html>
<html lang="en">
<head>
<meta charset="utf-8">
<title>KOLTA Black Grapes – Label</title>
<link rel="stylesheet" href="https://fonts.googleapis.com/css2?family=Bebas+Neue&family=Oswald:wght@400;600&display=swap">
<style>
  :root {
    --backdrop: #e9e9ea;
    --band-purple: #5a46a6;
    --panel-black-top: #0d0d11;
    --panel-black-bottom: #2b2934;
    --brand-teal: #1f9b93;
    --art-violet: #3b2f8c;
    --text-white: #f2f2f2;
  }
  * { margin: 0; padding: 0; box-sizing: border-box; }
  html, body {
    width: 1200px;
    height: 3182px;
    overflow: hidden;
    background: var(--backdrop);
  }
  .canvas {
    position: relative;
    width: 1200px;
    height: 3182px;
  }
  .label {
    position: absolute;
    left: 0;
    top: 1230px;
    width: 1200px;
    height: 723px;
    background: var(--band-purple);
    overflow: hidden;
  }
  .label-panel {
    position: absolute;
    inset: 0;
    width: 1200px;
    height: 723px;
  }
  .maker-name {
    position: absolute;
    left: 0;
    width: 946px;
    top: 34px;
    text-align: center;
    font-family: "Oswald", sans-serif;
    font-weight: 600;
    font-size: 44px;
    line-height: 1;
    color: var(--text-white);
    letter-spacing: 1px;
  }
  .product-name {
    position: absolute;
    left: 0;
    width: 946px;
    top: 96px;
    text-align: center;
    font-family: "Bebas Neue", sans-serif;
    font-size: 118px;
    line-height: 1;
    color: var(--brand-teal);
    letter-spacing: 4px;
  }
  .flavour-art {
    position: absolute;
    left: 272px;
    top: 205px;
    width: 420px;
    height: 370px;
    border-radius: 50%;
    background: radial-gradient(ellipse at 50% 50%, var(--brand-teal) 0%, var(--art-violet) 45%, rgba(59,47,140,0) 72%);
  }
  .flavour-name {
    position: absolute;
    left: 0;
    width: 946px;
    top: 582px;
    text-align: center;
    font-family: "Bebas Neue", sans-serif;
    font-size: 92px;
    line-height: 1;
    color: var(--text-white);
    letter-spacing: 2px;
  }
  .drink-type {
    position: absolute;
    left: 0;
    width: 946px;
    top: 668px;
    text-align: center;
    font-family: "Oswald", sans-serif;
    font-weight: 400;
    font-size: 24px;
    line-height: 1;
    color: var(--text-white);
    letter-spacing: 1px;
  }
</style>
</head>
<body>
<main class="canvas">
  <section class="label">
    <svg class="label-panel" viewBox="0 0 1200 723" aria-hidden="true">
      <defs>
        <linearGradient id="panelShade" x1="0" y1="0" x2="0" y2="1">
          <stop offset="0" stop-color="var(--panel-black-top)"/>
          <stop offset="1" stop-color="var(--panel-black-bottom)"/>
        </linearGradient>
      </defs>
      <path fill="url(#panelShade)"
        d="M123 0 C190 120 250 300 205 430 C170 530 70 610 51 723
           L672 723 C780 660 870 600 858 500 C846 400 760 330 790 205
           C810 115 850 50 846 0 Z"/>
    </svg>
    <div class="maker-name">kestrola</div>
    <h1 class="product-name">KOLTA</h1>
    <div class="flavour-art" role="img" aria-label="Illustration of a dancing figure surrounded by black grape bunches, leaves and bubbles"></div>
    <h2 class="flavour-name">BLACK GRAPES</h2>
    <p class="drink-type">FIZZY DRINK</p>
  </section>
</main>
</body>
</html>
```